Business Card Design

Need business card design for all carpentry & construction solutions. We would like to see designs that use black as a background with orange writing as it would stand out.

Business

RMP CONTRACTING
PETER LANGFORD
14 CALLOWAY ST
MARLOW CREEK
WA 6512
0487315962
rmpcontracting@kestrelmail.com

```html
<!DOCTYPE html>
<html lang="en">
<head>
<meta charset="utf-8">
<title>RMP Contracting – Business Card</title>
<link rel="stylesheet" href="https://fonts.googleapis.com/css2?family=Quicksand:wght@500;700&display=swap">
<style>
  :root {
    --stage: #2b2b2b;
    --card: #050505;
    --orange: #f7941d;
    --orange-soft: rgba(247, 148, 29, 0);
  }
  * { box-sizing: border-box; margin: 0; padding: 0; }
  html, body {
    width: 1200px;
    height: 799px;
    overflow: hidden;
    background: var(--stage);
    font-family: "Quicksand", sans-serif;
  }
  .stage {
    position: relative;
    width: 1200px;
    height: 799px;
  }
  .card {
    position: absolute;
    width: 520px;
    height: 297px;
    background: var(--card);
    color: var(--orange);
    box-shadow: 0 14px 30px rgba(0, 0, 0, 0.55);
  }
  .card--front { left: 50px; top: 251px; }
  .card--back { left: 630px; top: 251px; }

  .wordmark {
    font-weight: 700;
    color: var(--orange);
    letter-spacing: 0.02em;
    white-space: nowrap;
  }
  .card--front .wordmark {
    position: absolute;
    left: 0; right: 0;
    top: 50%;
    transform: translateY(-50%);
    text-align: center;
    font-size: 44px;
  }

  .back-brand {
    position: absolute;
    left: 0; top: 0;
    width: 260px;
    height: 100%;
    display: flex;
    align-items: center;
    justify-content: center;
  }
  .back-brand .wordmark { font-size: 22px; }

  .divider {
    position: absolute;
    left: 260px;
    top: 40px;
    width: 2px;
    height: 217px;
    background: linear-gradient(to bottom, var(--orange-soft), var(--orange) 40%, var(--orange) 60%, var(--orange-soft));
  }

  .contact {
    position: absolute;
    left: 282px;
    top: 62px;
    width: 228px;
  }
  .contact__name {
    font-weight: 700;
    font-size: 19px;
    letter-spacing: 0.03em;
    margin-bottom: 12px;
  }
  .contact__address {
    font-style: normal;
    font-weight: 500;
    font-size: 12px;
    line-height: 1.35;
    letter-spacing: 0.04em;
    padding-left: 8px;
    margin-bottom: 14px;
  }
  .contact__line {
    display: flex;
    align-items: center;
    gap: 8px;
    font-weight: 500;
    font-size: 11.5px;
    margin-bottom: 14px;
    white-space: nowrap;
  }
  .contact__line svg { flex: none; }
</style>
</head>
<body>
<main class="stage">
  <section class="card card--front" aria-label="Card front">
    <p class="wordmark">RMP CONTRACTING</p>
  </section>

  <section class="card card--back" aria-label="Card back">
    <div class="back-brand">
      <p class="wordmark">RMP CONTRACTING</p>
    </div>
    <div class="divider"></div>
    <div class="contact">
      <h1 class="contact__name">PETER LANGFORD</h1>
      <address class="contact__address">
        14 CALLOWAY ST<br>
        MARLOW CREEK<br>
        WA 6512
      </address>
      <p class="contact__line contact__line--phone">
        <svg width="18" height="18" viewBox="0 0 24 24" aria-hidden="true">
          <path d="M6.6 3.5l3 3.2-1.8 2.4c1.3 2.7 3.4 4.8 6.1 6.1l2.4-1.8 3.2 3-1.9 3.1C12 19 5 12 3.5 5.4z" fill="none" stroke="var(--orange)" stroke-width="1.5" stroke-linejoin="round"/>
        </svg>
        <span>0487315962</span>
      </p>
      <p class="contact__line contact__line--email">
        <svg width="18" height="14" viewBox="0 0 24 18" aria-hidden="true">
          <rect x="1" y="1" width="22" height="16" fill="none" stroke="var(--orange)" stroke-width="1.5"/>
          <path d="M1 1l11 9 11-9M1 17l8-7M23 17l-8-7" fill="none" stroke="var(--orange)" stroke-width="1.5"/>
        </svg>
        <span>rmpcontracting@kestrelmail.com</span>
      </p>
    </div>
  </section>
</main>
</body>
</html>
```